Business software developers new website

We need to redesign our website. Our current website is http://www.plumvista.net/index.html, which is outdated and needs a new look. We moved out from web design and have concentrated more on the back end of the systems, for example, system support and security and cloud-based applications. Our major clients include both private and government sectors. We would like to see some designs that are all in one page, simple and clean. Prefer illustrator or obstructed images instead of real-life photos. Must look futuristic yet friendly. Attached the new logo for your references and good luck.

Target Market(s)

Medium to big company for their IT or data management. Either improve or upgrade their current system.

Industry/Entity Type

Business Software

Number of Pages Required

1 page

Colors

Designer to choose colors to be used in the design.

Requirements
Must have
• Simple and clean. Individual assets must be provided in the correct size and format(png or jpeg). Prefer Goggle fonts. Even though the logo color is red, grey and black, still prefer some modern colors that go well with red. When design, must consider the possibility to convert it into responsive.
Nice to have
• White background
Should not have
• real life photos, no slider

```html
<!DOCTYPE html>
<html lang="en">
<head>
<meta charset="utf-8">
<title>plumvista.net – Business Software</title>
<link rel="stylesheet" href="https://fonts.googleapis.com/css2?family=Roboto+Condensed:wght@300;400;700&family=Roboto:wght@400;500;700&display=swap">
<style>
:root{
  --red:#d8112f;
  --red-dark:#c10b27;
  --navy:#1f2346;
  --blue:#0d3f86;
  --ink:#1b1b1b;
  --text:#555;
  --muted:#777;
  --grey-bg:#f4f4f4;
  --faint:#ececec;
  --white:#fff;
}
*{box-sizing:border-box;margin:0;padding:0}
html,body{width:1200px;height:3179px;overflow:hidden}
body{position:relative;background:var(--white);font-family:'Roboto',Arial,sans-serif;color:var(--text)}
.abs{position:absolute}
.cond{font-family:'Roboto Condensed','Arial Narrow',sans-serif}
.brand{font-family:'Roboto Condensed','Arial Narrow',sans-serif;font-weight:300;color:var(--ink);letter-spacing:.5px;white-space:nowrap}
.brand .dot{display:inline-block;width:.18em;height:.18em;border-radius:50%;background:currentColor;vertical-align:middle;margin:0 .06em}

/* header */
.site-brand{left:146px;top:20px;font-size:46px}
.nav{top:40px;font-size:17px;color:var(--ink);font-family:'Roboto',sans-serif}
.login{left:950px;top:31px;width:105px;height:40px;border-radius:20px;background:var(--navy);color:#fff;font-size:16px;display:flex;align-items:center;justify-content:center;gap:8px}

/* hero */
.hero-bg{left:0;top:80px;width:1200px;height:620px}
.hero-brand{left:599px;top:228px;font-size:66px;color:#fff}
.hero-sub{left:599px;top:318px;width:390px;font-size:17px;line-height:24px;color:#fff;font-weight:500}
.btn-ghost{left:600px;top:391px;width:131px;height:41px;border:2px solid #fff;border-radius:21px;color:#fff;font-size:14px;font-weight:500;display:flex;align-items:center;justify-content:center}

/* feature circles */
.bubble{width:280px;height:280px;border-radius:50%;background:#fff;border-top:9px solid var(--red);text-align:center;padding-top:50px}
.bubble h3{font-family:'Roboto Condensed',sans-serif;font-weight:700;font-size:24px;color:var(--ink);margin-bottom:12px}
.bubble p{font-size:11px;line-height:24px;color:var(--text);width:210px;margin:0 auto}
.pill-navy{display:inline-block;margin-top:14px;background:var(--navy);color:#fff;font-size:12px;font-weight:700;padding:10px 16px;border-radius:18px}
.bubble.main{width:330px;height:330px;border:none;background:linear-gradient(160deg,#e72a43,var(--red-dark));padding-top:60px;box-shadow:0 10px 25px rgba(200,10,40,.25)}
.bubble.main h3{color:#fff;font-size:29px}
.bubble.main p{color:#fff;font-size:13px;line-height:28px;width:260px}
.pill-white{display:inline-block;margin-top:14px;background:#fff;color:var(--red);font-size:15px;font-weight:500;padding:11px 25px;border-radius:20px}

/* section titles */
.ghost{font-family:'Roboto Condensed',sans-serif;font-weight:700;color:var(--faint);line-height:1;white-space:nowrap}
.title{font-family:'Roboto Condensed',sans-serif;line-height:1;white-space:nowrap}
.title b{font-weight:700;color:var(--ink)}
.title span{font-weight:300;color:var(--red)}

/* about */
.about-copy{left:225px;top:1096px;width:450px;font-size:13px;line-height:26.5px;color:var(--text)}
.btn-navy{left:225px;top:1334px;width:144px;height:46px;border-radius:23px;background:var(--navy);color:#fff;font-size:13px;font-weight:700;display:flex;align-items:center;justify-content:center;gap:7px}
.about-art{left:753px;top:889px;width:447px;height:568px;background:radial-gradient(ellipse at 55% 45%,#dbe9f9 0%,#eef3f8 45%,#f7f7f7 75%,rgba(247,247,247,0) 100%)}

/* services */
.card{width:413px;height:149px;border-radius:75px;background:#fff;box-shadow:0 4px 12px rgba(0,0,0,.18),inset 0 0 0 4px #f1f1f1}
.card .badge{position:absolute;left:6px;top:6px;width:137px;height:137px;border-radius:69px 0 0 69px;display:flex;align-items:center;justify-content:center}
.card .badge::after{content:"";position:absolute;right:-6px;top:67px;width:14px;height:3px;background:inherit}
.badge.red{background:linear-gradient(135deg,#e51c3b,#b9071f)}
.badge.grey{background:linear-gradient(135deg,#8b8b8b,#5f5f5f)}
.card h4{position:absolute;left:166px;top:30px;font-size:16px;font-weight:500;color:var(--ink);letter-spacing:.2px}
.card p{position:absolute;left:166px;top:58px;width:225px;font-size:12px;line-height:21px;color:var(--muted)}

/* contact */
.contact-intro{left:522px;top:2200px;width:510px;font-size:12.5px;line-height:24px;color:var(--text)}
.field{background:#fff;box-shadow:0 2px 8px rgba(0,0,0,.12);font-size:13px;color:#555;padding:20px 20px}
.btn-red{left:143px;top:2600px;width:177px;height:50px;border-radius:25px;background:var(--red);color:#fff;font-size:15px;font-weight:500;display:flex;align-items:center;justify-content:center}

/* footer */
.foot-brand{left:0;width:1200px;top:2808px;text-align:center;font-size:50px}
.foot-h{top:2908px;font-family:'Roboto Condensed',sans-serif;font-size:19px;font-weight:400;color:var(--ink)}
.foot-list{font-size:11.5px;line-height:16px;color:#444}
.foot-list li{list-style:none;display:flex;gap:10px;align-items:flex-start}
.links li{margin-bottom:6.8px}
.links li::before{content:"»";color:var(--red);width:14px}
.affiliate{left:578px;top:2951px;width:170px;height:49px;border:2px solid var(--ink);display:flex;align-items:center;justify-content:center;font-family:'Roboto Condensed',sans-serif;font-size:22px;font-weight:700;color:var(--ink)}
.social{top:3018px;width:27px;height:27px;border-radius:50%}
.news-input{left:824px;top:2980px;width:231px;height:37px;background:#fff;box-shadow:0 2px 6px rgba(0,0,0,.15);font-size:12px;color:#333;padding:11px 16px}
.subscribe{left:824px;top:3025px;width:97px;height:37px;background:var(--red);color:#fff;font-size:13px;font-weight:500;display:flex;align-items:center;justify-content:center}
.rule{left:143px;top:3117px;width:913px;height:1px;background:#cfcfcf}
.legal{top:3145px;font-size:11px;color:#555}
</style>
</head>
<body>

<!-- header -->
<div class="abs brand site-brand">plumvista<span class="dot"></span>net</div>
<div class="abs nav" style="left:535px">Home</div>
<div class="abs nav" style="left:614px">Our Services</div>
<div class="abs nav" style="left:742px">Our Clients</div>
<div class="abs nav" style="left:859px">Contact</div>
<div class="abs login">
  <svg width="12" height="14" viewBox="0 0 12 14"><circle cx="6" cy="3.5" r="3.3" fill="#fff"/><path d="M0 14c0-4 2.5-6 6-6s6 2 6 6z" fill="#fff"/></svg>LOGIN
</div>

<!-- hero -->
<svg class="abs hero-bg" viewBox="0 80 1200 620" width="1200" height="620" role="img" aria-label="Futuristic digital hand made of network lines touching a glowing dotted globe on a deep blue background">
  <defs>
    <radialGradient id="heroGlow" cx="0.42" cy="0.6" r="0.75">
      <stop offset="0" stop-color="#2d8de3"/>
      <stop offset="0.45" stop-color="#0f4f9c"/>
      <stop offset="1" stop-color="#0a2a63"/>
    </radialGradient>
  </defs>
  <path d="M0 222 Q600 -36 1200 222 L1200 700 L0 700 Z" fill="#d8112f"/>
  <path d="M0 248 Q600 -8 1200 248 L1200 700 L0 700 Z" fill="url(#heroGlow)"/>
</svg>
<div class="abs brand hero-brand">plumvista<span class="dot"></span>net</div>
<div class="abs hero-sub">Sed ut perspiciatis unde omnis iste natus error sit voluptatem accusantium doloremque</div>
<div class="abs btn-ghost">READ MORE</div>

<div class="abs bubble" style="left:160px;top:556px">
  <h3>ABOUT US</h3>
  <p>We have provided web design, graphic design and application development solutions for a wide variety of industries. We are known for the quality</p>
  <span class="pill-navy">READ MORE</span>
</div>
<div class="abs bubble main" style="left:435px;top:528px">
  <h3>OUR CLIENTS</h3>
  <p>We undertake many projects from small businesses to large corporations. We are also extremely experienced in the long term support of comprehensive web based</p>
  <span class="pill-white">READ MORE</span>
</div>
<div class="abs bubble" style="left:760px;top:556px">
  <h3>NEWS</h3>
  <p>Sed ut perspiciatis unde omnis iste natus error sit voluptatem accusantium doloremque laudantium, totam rem aperiam, eaque ipsa quae ab illo inventore</p>
  <span class="pill-navy">READ MORE</span>
</div>

<!-- about -->
<div class="abs ghost" style="left:0;top:938px;font-size:110px">ABOUT</div>
<div class="abs title" style="left:225px;top:968px;font-size:48px"><b>ABOUT</b></div>
<div class="abs title" style="left:225px;top:1022px;font-size:50px"><span>Plumvista.net</span></div>
<p class="abs about-copy">Plumvista.net is an Australian based Software and Web Development Company that provides individual technology solutions and professional software for clients worldwide.<br>Our work is based on quality sales, customer and technical support services. Being oriented towards innovative productivity in our work, we come up with essential tools for online business enhancing. Our programming specialists focus on delivering solutions for small start-ups as well as large organizations and companies.</p>
<div class="abs btn-navy">READ MORE
  <svg width="13" height="13" viewBox="0 0 13 13"><circle cx="6.5" cy="6.5" r="6.5" fill="#fff"/><path d="M5 3.5l3 3-3 3" stroke="#1f2346" stroke-width="1.8" fill="none"/></svg>
</div>

<!-- services background -->
<svg class="abs" style="left:0;top:1380px" width="1200" height="780" viewBox="0 1380 1200 780">
  <path d="M0 1395 Q380 1463 760 1463 L1200 1463 L1200 2087 Q900 2060 420 2087 Q200 2100 0 2136 Z" fill="#f4f4f4"/>
  <path d="M0 1395 Q380 1463 760 1463" stroke="#d8112f" stroke-width="6" fill="none"/>
  <path d="M420 2087 Q900 2060 1200 2155" stroke="#d8112f" stroke-width="7" fill="none"/>
</svg>
<div class="abs about-art" role="img" aria-label="Isometric illustration of a developer working at a desk with code screens labelled XML, PHP, SQL and CSS, gears and a wifi symbol"></div>

<div class="abs ghost" style="left:0;width:1200px;text-align:center;top:1538px;font-size:98px;color:#e8e8e8">SERVICES</div>
<div class="abs title" style="left:0;width:1200px;text-align:center;top:1582px;font-size:50px"><b>OUR</b> <span>Services</span></div>

<div class="abs card" style="left:170px;top:1673px">
  <div class="badge red">
    <svg width="66" height="66" viewBox="0 0 66 66" fill="none" stroke="#fff" stroke-width="2"><rect x="6" y="16" width="54" height="34" rx="2"/><path d="M26 58h14M33 50v8"/><path d="M33 22l10 5v11l-10 5-10-5V27z"/><path d="M23 27l10 5 10-5M33 32v11"/><circle cx="20" cy="6" r="2"/><circle cx="33" cy="4" r="2"/><circle cx="46" cy="6" r="2"/><path d="M20 8v8M33 6v10M46 8v8"/></svg>
  </div>
  <h4>SED UT PERSPICIATIS</h4>
  <p>Sed ut perspiciatis unde omnis iste natus error sit voluptatem accusantium doloremqaudantiumue..</p>
</div>
<div class="abs card" style="left:615px;top:1673px">
  <div class="badge grey">
    <svg width="70" height="66" viewBox="0 0 70 66" fill="none" stroke="#fff" stroke-width="2"><path d="M6 20L35 5l29 15z"/><path d="M8 24h54M8 56h54M4 62h62"/><path d="M14 28v24M24 28v24M35 28v24M46 28v24M56 28v24"/></svg>
  </div>
  <h4>ISTE NATUS ERROR</h4>
  <p>Sed ut perspiciatis unde omnis iste natus error sit voluptatem accusantium doloremqaudantiumue..</p>
</div>
<div class="abs card" style="left:170px;top:1852px">
  <div class="badge grey">
    <svg width="56" height="68" viewBox="0 0 56 68" fill="none" stroke="#fff" stroke-width="2.2"><path d="M6 4h32l12 12v48H6z"/><path d="M38 4v12h12"/><rect x="18" y="36" width="20" height="16" rx="1"/><path d="M22 36v-5a6 6 0 0 1 12 0v5"/></svg>
  </div>
  <h4>NEQUE PORRO QUISQU</h4>
  <p>Sed ut perspiciatis unde omnis iste natus error sit voluptatem accusantium doloremqaudantiumue..</p>
</div>
<div class="abs card" style="left:615px;top:1852px">
  <div class="badge red">
    <svg width="68" height="68" viewBox="0 0 68 68" fill="none" stroke="#fff" stroke-width="2"><rect x="6" y="6" width="46" height="56"/><path d="M6 16h46M14 26h18M14 34h14M14 42h12M14 50h10"/><path d="M58 18l6 6-24 26-8 2 2-8z"/></svg>
  </div>
  <h4>ULLAM CORPORIS</h4>
  <p>Sed ut perspiciatis unde omnis iste natus error sit voluptatem accusantium doloremqaudantiumue..</p>
</div>

<!-- contact -->
<div class="abs ghost" style="left:0;top:2200px;font-size:98px">CONTACT</div>
<div class="abs title" style="left:143px;top:2224px;font-size:50px"><b>QUICK</b> <span>Contact</span></div>
<p class="abs contact-intro">As web developers, we understand that a powerful and functional web site is a vital component of modern day marketing for companies of today. This is why our web site development team work with all of our clients to ensure their web site design will deliver to their target market.</p>
<div class="abs field" style="left:143px;top:2340px;width:426px;height:51px;padding-top:18px">Enter Name</div>
<div class="abs field" style="left:583px;top:2340px;width:426px;height:51px;padding-top:18px">Enter Email</div>
<div class="abs field" style="left:143px;top:2408px;width:426px;height:49px;padding-top:17px">Phone</div>
<div class="abs field" style="left:583px;top:2408px;width:426px;height:49px;padding-top:17px">Where I can Reply?</div>
<div class="abs field" style="left:143px;top:2475px;width:866px;height:87px;padding-top:18px">Talk to me</div>
<div class="abs btn-red">SEND MESSAGE</div>

<!-- footer -->
<svg class="abs" style="left:0;top:2720px" width="1200" height="459" viewBox="0 2720 1200 459">
  <path d="M0 2852 Q600 2620 1200 2852 L1200 3179 L0 3179 Z" fill="#f4f4f4"/>
  <path d="M0 2852 Q600 2620 1200 2852" stroke="#c9c9c9" stroke-width="7" fill="none"/>
</svg>
<div class="abs brand foot-brand">plumvista<span class="dot"></span>net</div>

<div class="abs foot-h" style="left:144px">CONTACT INFO</div>
<ul class="abs foot-list" style="left:144px;top:2950px;width:210px">
  <li style="margin-bottom:10px"><svg width="14" height="18" viewBox="0 0 14 18" fill="none" stroke="#d8112f" stroke-width="1.5"><path d="M7 17s6-6 6-10A6 6 0 0 0 1 7c0 4 6 10 6 10z"/><circle cx="7" cy="7" r="2"/></svg><span>232,Lorem Ipsum is simply dummy text.</span></li>
  <li style="margin-bottom:10px"><svg width="16" height="16" viewBox="0 0 16 16" fill="none" stroke="#d8112f" stroke-width="1.5"><path d="M3 1l3 3-2 2a10 10 0 0 0 6 6l2-2 3 3-2 2C7 15 1 9 1 3z"/></svg><span>CALL US: 1 888 888 8888</span></li>
  <li><svg width="16" height="14" viewBox="0 0 16 14" fill="none" stroke="#d8112f" stroke-width="1.5"><rect x="1" y="2" width="14" height="10"/><path d="M1 2l7 6 7-6"/></svg><span>info@companyname.com</span></li>
</ul>

<div class="abs foot-h" style="left:390px">QUICK LINKS</div>
<ul class="abs foot-list links" style="left:390px;top:2950px">
  <li>Home</li><li>About us</li><li>Services</li><li>Clients</li><li>Contact us</li>
</ul>

<div class="abs foot-h" style="left:575px">AFFILIATES</div>
<div class="abs affiliate">Nexor Studio</div>
<div class="abs social" style="left:575px;background:#1f2346"></div>
<div class="abs social" style="left:609px;background:#1d8fd8"></div>
<div class="abs social" style="left:643px;background:#d8112f"></div>
<div class="abs social" style="left:677px;background:#9c7a46"></div>
<div class="abs social" style="left:711px;background:#1a5f9e"></div>

<div class="abs foot-h" style="left:824px">SIGN UP NEWSLETTER</div>
<div class="abs foot-list" style="left:824px;top:2950px">Lorem ipsum dolor sit aconsectetur</div>
<div class="abs news-input">Enter Email</div>
<div class="abs subscribe">SUBSCRIBE</div>

<div class="abs rule"></div>
<div class="abs legal" style="left:143px">Copyrights © 2019, Companyname. All rights reserved</div>
<div class="abs legal" style="left:847px">Privacy policy&nbsp; / &nbsp;Terms and conditions</div>

</body>
</html>
```